Business Card Design Project

We are not a new company, but renamed to "Norvanta Kitchens" last year. We specialize in modern high-end cabinetry imports. We would like to communicate a sense of quality and cutting edge technology. Ideally the design would incorporate our logo colors, silver, red and preferably a black, matte background. Though we are open to suggestions.
Logo is attached.
Edit: I have attached rough drafts of the previous cards, this way you will have all necessary content that needs to go on the cards.
Reason: We have received a lot of great designs, but due to the sheer number we couldn't respond to all. We will extend the deadline for another 7 days to finalize and provide feedback to designers.
Thank you for your hard work!
Industry/Entity Type
Business
Look and feel
Each slider illustrates characteristics of the customer's brand and the style your logo design should communicate.

```html
<!DOCTYPE html>
<html lang="en">
<head>
<meta charset="utf-8">
<title>Norvanta Kitchens – Business Card</title>
<link rel="stylesheet" href="https://fonts.googleapis.com/css2?family=Lato:wght@400;700&family=Oranienbaum&family=Open+Sans:wght@400&display=swap">
<style>
  :root {
    --stage: #d8d3cb;
    --card: #242223;
    --red: #ee1c25;
    --silver: #c8c8c8;
    --white: #f2f2f2;
    --rule: #8a8a8a;
  }
  * { box-sizing: border-box; margin: 0; padding: 0; }
  html, body { width: 1200px; height: 891px; overflow: hidden; background: var(--stage); }
  .stage { position: relative; width: 1200px; height: 891px; }

  .card {
    position: absolute;
    left: 260px;
    width: 680px;
    height: 389px;
    background: var(--card);
    box-shadow: 0 6px 18px rgba(0,0,0,0.25);
    overflow: hidden;
  }
  .card--front { top: 40px; }
  .card--back { top: 462px; }

  .accent-bar { position: absolute; top: 78px; width: 23px; height: 235px; background: var(--red); }
  .accent-bar--left { left: 0; }
  .accent-bar--right { right: 0; }

  .brand {
    position: absolute;
    display: flex; align-items: center; gap: 10px;
    font-family: "Lato", sans-serif;
    font-weight: 400;
    color: var(--silver);
    text-transform: uppercase;
    white-space: nowrap;
  }
  .brand__mark { background: var(--silver); flex: none; }
  .card--front .brand { left: 54px; top: 70px; font-size: 21px; letter-spacing: 3px; }
  .card--front .brand__mark { width: 16px; height: 16px; }
  .card--back .brand { left: 50%; top: 50%; transform: translate(-50%, -50%); font-size: 30px; letter-spacing: 4px; gap: 14px; }
  .card--back .brand__mark { width: 22px; height: 22px; }

  .person { position: absolute; right: 395px; top: 212px; text-align: right; }
  .person__name {
    font-family: "Oranienbaum", serif;
    font-size: 56px; line-height: 1;
    color: var(--white);
    transform: scaleX(0.82); transform-origin: right;
    white-space: nowrap;
  }
  .person__role {
    font-family: "Open Sans", sans-serif;
    font-size: 14px; color: var(--red); margin-top: 4px;
  }

  .divider { position: absolute; left: 341px; top: 138px; width: 1px; height: 212px; background: var(--rule); }

  .contacts { position: absolute; left: 366px; top: 163px; list-style: none; }
  .contact {
    display: flex; align-items: center; gap: 9px;
    height: 29.6px;
    font-family: "Open Sans", sans-serif;
    font-size: 14.5px; color: var(--white);
    white-space: nowrap;
  }
  .contact__icon { width: 20px; height: 20px; flex: none; }
</style>
</head>
<body>
<main class="stage">

  <section class="card card--front" aria-label="Business card front">
    <div class="accent-bar accent-bar--left"></div>
    <div class="accent-bar accent-bar--right"></div>

    <div class="brand"><span class="brand__mark"></span>Norvanta Kitchens</div>

    <div class="person">
      <div class="person__name">Adrian Velko</div>
      <div class="person__role">Director</div>
    </div>

    <div class="divider"></div>

    <ul class="contacts">
      <li class="contact">
        <svg class="contact__icon" viewBox="0 0 20 20" aria-hidden="true"><rect width="20" height="20" rx="3" fill="#ee1c25"/><path d="M10 3.5a4 4 0 0 0-4 4c0 3 4 8 4 8s4-5 4-8a4 4 0 0 0-4-4z" fill="#fff"/><circle cx="10" cy="7.5" r="1.5" fill="#ee1c25"/></svg>
        2180 - 84 St, Edmonton, AB T6C 3N1
      </li>
      <li class="contact">
        <svg class="contact__icon" viewBox="0 0 20 20" aria-hidden="true"><rect width="20" height="20" rx="3" fill="#ee1c25"/><path d="M3.5 8c0-2 3-3.5 6.5-3.5S16.5 6 16.5 8l-2.5.6-.5-1.6h-7l-.5 1.6z" fill="#fff"/><path d="M6 10h8l1.5 5.5h-11z" fill="#fff"/><circle cx="10" cy="12.6" r="1.4" fill="#ee1c25"/></svg>
        +780.555.0142
      </li>
      <li class="contact">
        <svg class="contact__icon" viewBox="0 0 20 20" aria-hidden="true"><rect width="20" height="20" rx="3" fill="#ee1c25"/><rect x="6" y="3.5" width="8" height="4" fill="#fff"/><rect x="3.5" y="8" width="13" height="6" rx="1" fill="#fff"/><rect x="6" y="12" width="8" height="4.5" fill="#fff" stroke="#ee1c25" stroke-width="1"/></svg>
        +780.555.0176
      </li>
      <li class="contact">
        <svg class="contact__icon" viewBox="0 0 20 20" aria-hidden="true"><rect width="20" height="20" rx="3" fill="#ee1c25"/><rect x="6" y="3" width="8" height="14" rx="1.5" fill="#fff"/><rect x="7.3" y="4.8" width="5.4" height="4" fill="#ee1c25"/><circle cx="10" cy="14.5" r="1" fill="#ee1c25"/></svg>
        +780.555.0193
      </li>
      <li class="contact">
        <svg class="contact__icon" viewBox="0 0 20 20" aria-hidden="true"><rect width="20" height="20" rx="3" fill="#ee1c25"/><rect x="3.5" y="5.5" width="13" height="9" fill="#fff"/><path d="M3.5 5.5l6.5 5 6.5-5M3.5 14.5l4.6-4.6M16.5 14.5l-4.6-4.6" fill="none" stroke="#ee1c25" stroke-width="1"/></svg>
        adrian@norvantakitchens.com
      </li>
      <li class="contact">
        <svg class="contact__icon" viewBox="0 0 20 20" aria-hidden="true"><rect width="20" height="20" rx="3" fill="#ee1c25"/><g fill="none" stroke="#fff" stroke-width="1.2"><circle cx="10" cy="10" r="6"/><ellipse cx="10" cy="10" rx="2.6" ry="6"/><path d="M4 10h12M5 7h10M5 13h10"/></g></svg>
        www.norvantakitchens.com
      </li>
    </ul>
  </section>

  <section class="card card--back" aria-label="Business card back">
    <div class="brand"><span class="brand__mark"></span>Norvanta Kitchens</div>
  </section>

</main>
</body>
</html>
```